HomeBridle business card and stationary design

We are looking for a simple yet elegant design for our mortgage company business card and stationary.

The card should include:
Name (Derek Walsh)
Title (CEO)
Phone Number (614-208-3917)
Address (48 Birchfield Court, Suite 314, Marlow, OH 43952)
Email (email@homebridle-example.com)
"NMLS" i.e. (NMLS 61947)
"Company NMLS" (Company NMLS 472815)

See above

```html
<!DOCTYPE html>
<html lang="en">
<head>
<meta charset="utf-8">
<title>HomeBridle Business Card</title>
<link href="https://fonts.googleapis.com/css2?family=Montserrat:wght@400;500;600&display=swap" rel="stylesheet">
<style>
  :root {
    --backdrop: #e9eaec;
    --card-white: #ffffff;
    --card-navy: #1b2631;
    --accent-blue: #1fa3dd;
    --text-grey: #4a4f55;
    --logo-silver: #a7acb1;
  }
  * { box-sizing: border-box; margin: 0; padding: 0; }
  html, body {
    width: 1200px; height: 913px; overflow: hidden;
    background: var(--backdrop);
    font-family: "Montserrat", sans-serif;
  }
  .stage {
    position: relative; width: 1200px; height: 913px;
    display: flex; flex-direction: column; align-items: center; justify-content: center; gap: 56px;
  }
  .card {
    position: relative; width: 600px; height: 343px;
    border-bottom: 4px solid var(--accent-blue);
    box-shadow: 0 6px 18px rgba(0,0,0,0.18);
  }
  .card--front { background: var(--card-white); }
  .card--back {
    background: var(--card-navy);
    display: flex; align-items: center; justify-content: center;
  }
  .identity {
    position: absolute; right: 300px; top: 150px;
    text-align: right;
  }
  .identity__name {
    color: var(--accent-blue); font-weight: 600; font-size: 34px;
    letter-spacing: 0.5px; line-height: 1; text-transform: uppercase;
  }
  .identity__title {
    color: var(--text-grey); font-weight: 400; font-size: 15px; margin-top: 4px;
  }
  .divider {
    position: absolute; left: 316px; top: 112px;
    width: 1px; height: 104px; background: var(--accent-blue);
  }
  .details {
    position: absolute; left: 330px; top: 98px;
    color: var(--text-grey); font-size: 12.5px; line-height: 1.45; font-weight: 400;
  }
  .details__row { display: flex; align-items: center; gap: 5px; white-space: nowrap; }
  .details__icon { width: 10px; height: 10px; flex: none; }
  .brand-name {
    color: var(--logo-silver); font-weight: 500; font-size: 64px; letter-spacing: -0.5px;
  }
</style>
</head>
<body>
  <main class="stage">
    <section class="card card--front" aria-label="Business card front">
      <div class="identity">
        <p class="identity__name">Derek Walsh</p>
        <p class="identity__title">CEO</p>
      </div>
      <div class="divider"></div>
      <div class="details">
        <p class="details__row">NMLS 61947</p>
        <p class="details__row">Company NMLS 472815</p>
        <p class="details__row">48 Birchfield Court,</p>
        <p class="details__row">Suite 314, Marlow, OH 43952</p>
        <p class="details__row">
          <svg class="details__icon" viewBox="0 0 10 10" aria-hidden="true"><path d="M2 1 L3.6 1 L4.2 3 L3.2 3.8 Q4 5.8 6.2 6.8 L7 5.8 L9 6.4 L9 8 Q8.6 9 7.5 9 Q1 8 1 2 Q1 1 2 1 Z" fill="#1fa3dd"/></svg>
          614-208-3917
        </p>
        <p class="details__row">
          <svg class="details__icon" viewBox="0 0 10 10" aria-hidden="true"><rect x="0.8" y="2" width="8.4" height="6" fill="none" stroke="#1fa3dd" stroke-width="1"/><path d="M0.8 2 L5 5.4 L9.2 2" fill="none" stroke="#1fa3dd" stroke-width="1"/></svg>
          email@homebridle-example.com
        </p>
      </div>
    </section>
    <section class="card card--back" aria-label="Business card back">
      <p class="brand-name">HomeBridle</p>
    </section>
  </main>
</body>
</html>
```